Magnetic Business card Design do a service provider

Hi,

The company aim is to provide all service needs under one roof. However, at the moment there is only Accounting, Electrical and IT branches. There will be more services coming onboard in the future.

I already have a logo designed (Company name is already part of the logo), I now need a magnetic business card designed.

The business card will contain the following:

- Company Logo
- Contact#
- E-mail
- enough space to add website URL (for future)
Updates

Project Deadline Extended Reason: HI All,The deadline has been extended due to not having enough time to review an overwhelming number of designs that has been submitted by lots of designers.I will be uploading a draft of designs that i have in mind.Thanks. Added Friday, January 22, 2016

Target Market(s)

Residential, Home-based Businesses, Small and Medium businesses

Industry/Entity Type

Business

Contact Information for Business Card

Contact#: 0491 738 552
E-mail: service@brightharborgroup.net.au

Font styles to use
Decorative
Script

Requirements
Must have
• Round edges
• Some form of logo incorporation as a background

```html
<!DOCTYPE html>
<html lang="en">
<head>
<meta charset="utf-8">
<title>Bright Harbor Group – Business Card</title>
<link href="https://fonts.googleapis.com/css2?family=Lato:wght@400;700&display=swap" rel="stylesheet">
<style>
  :root {
    --stage: #1f1f21;
    --card-top: #9a9da2;
    --card-bottom: #7f8287;
    --card-edge: rgba(255,255,255,0.35);
    --brand-blue: #1f7fd4;
    --icon-blue: #1d6fc0;
    --ink: #111417;
    --panel: rgba(255,255,255,0.94);
    --mark-teal: rgba(96,168,188,0.45);
  }
  * { margin: 0; padding: 0; box-sizing: border-box; }
  html, body {
    width: 1200px; height: 900px; overflow: hidden;
    background: var(--stage);
    font-family: "Lato", Arial, sans-serif;
  }
  .card {
    position: absolute;
    left: 110px; top: 170px;
    width: 980px; height: 560px;
    border-radius: 34px;
    background: linear-gradient(160deg, var(--card-top), var(--card-bottom));
    border: 2px solid var(--card-edge);
    overflow: hidden;
  }
  .background-mark {
    position: absolute;
    left: 470px; top: 60px;
    width: 440px; height: 440px;
    border-radius: 50%;
    background: var(--mark-teal);
  }
  .brand {
    position: absolute;
    left: 150px; top: 140px;
    display: flex; align-items: center; gap: 16px;
  }
  .brand-dot {
    width: 34px; height: 34px; border-radius: 50%;
    background: var(--brand-blue);
  }
  .brand-name {
    font-weight: 700; font-size: 38px;
    color: var(--brand-blue);
  }
  .contact-panel {
    position: absolute;
    left: 430px; top: 230px;
    width: 550px; height: 220px;
    background: var(--panel);
    padding: 24px 30px;
    color: var(--ink);
  }
  .person-name { font-size: 26px; line-height: 30px; }
  .person-title { font-size: 21px; line-height: 28px; margin-bottom: 8px; }
  .contact-list { list-style: none; }
  .contact-list li {
    display: flex; align-items: center; gap: 10px;
    font-size: 20px; line-height: 25px;
  }
  .contact-icon { width: 17px; height: 17px; flex: none; }
</style>
</head>
<body>
  <div class="card">
    <div class="background-mark" role="img" aria-label="Faint background brand mark area"></div>

    <div class="brand">
      <span class="brand-dot"></span>
      <span class="brand-name">Bright Harbor Group</span>
    </div>

    <div class="contact-panel">
      <p class="person-name">Your name here</p>
      <p class="person-title">Title here</p>
      <ul class="contact-list">
        <li>
          <svg class="contact-icon" viewBox="0 0 16 16"><rect width="16" height="16" rx="3" fill="var(--icon-blue)"/><path d="M8 3a3 3 0 0 0-3 3c0 2.3 3 6 3 6s3-3.7 3-6a3 3 0 0 0-3-3zm0 4.2A1.2 1.2 0 1 1 8 4.8a1.2 1.2 0 0 1 0 2.4z" fill="#fff"/></svg>
          Address here, address here,ad556
        </li>
        <li>
          <svg class="contact-icon" viewBox="0 0 16 16"><rect width="16" height="16" rx="3" fill="var(--icon-blue)"/><path d="M5 3.5l2 2-1 1.2a6 6 0 0 0 3.3 3.3l1.2-1 2 2-1.3 1.5C7.5 12.3 3.7 8.5 3.5 4.8z" fill="#fff"/></svg>
          0491 738 552
        </li>
        <li>
          <svg class="contact-icon" viewBox="0 0 16 16"><rect width="16" height="16" rx="3" fill="var(--icon-blue)"/><rect x="3" y="4.5" width="10" height="7" fill="#fff"/><path d="M3 4.5l5 4 5-4" fill="none" stroke="var(--icon-blue)" stroke-width="1.2"/></svg>
          service@brightharborgroup.net.au
        </li>
        <li>
          <svg class="contact-icon" viewBox="0 0 16 16"><rect width="16" height="16" rx="3" fill="var(--icon-blue)"/><circle cx="8" cy="8" r="4.5" fill="none" stroke="#fff" stroke-width="1.2"/><path d="M3.5 8h9M8 3.5c-2 2.5-2 6.5 0 9M8 3.5c2 2.5 2 6.5 0 9" fill="none" stroke="#fff" stroke-width="1"/></svg>
          www. yourwebsite.com
        </li>
      </ul>
    </div>
  </div>
</body>
</html>
```